One page sales fact sheet for data consultancy company

We need a serious and professional looking 1-page fact sheet that we want to send over to potential clients via email.
The upper part should consists of a header, the client logo and 3 charts.
(1 chart with 5 datapoints / 1 chart with 3 bubbles and percentage in it, 1 chart with numbers and text)
In the lower part there should be some text description about our company and a big chart consisting of a table (see drawing).
See attached drawing to get a better understanding of the whole idea.
The fact sheet should be catchy but professional in the same way.
Colors your choice but classic, i.e. black/white/grey/blue
The contest winner can expect more work from us based on the winning design.
*Please note that the logo reflects our original logo style but is not our
actual company name for privacy reasons

```html
<!DOCTYPE html>
<html lang="en">
<head>
<meta charset="utf-8">
<title>ORVEN – Market Analysis Fact Sheet</title>
<link rel="stylesheet" href="https://fonts.googleapis.com/css2?family=Montserrat:wght@300;400;700&family=Roboto:ital,wght@0,400;1,300;1,700;1,900&family=Source+Sans+3:wght@400&display=swap">
<style>
  :root {
    --ink: #232833;
    --ink-soft: #2c3240;
    --ink-band: #323846;
    --paper: #ffffff;
    --aqua: #93dfe2;
    --steel: #8e9095;
    --mist: #e4e5e7;
    --ghost: #bfc1c5;
    --faint: #4a5262;
  }
  * { margin: 0; padding: 0; box-sizing: border-box; }
  html, body { width: 849px; height: 1200px; overflow: hidden; background: var(--paper); }
  .sheet { position: relative; width: 849px; height: 1200px; background: var(--paper); color: var(--paper); }
  .shapes { position: absolute; inset: 0; }
  .abs { position: absolute; white-space: nowrap; line-height: 1; }
  .center { transform: translateX(-50%); text-align: center; }

  .brand { font-family: "Montserrat", sans-serif; font-weight: 700; font-size: 88px; letter-spacing: 2px; color: var(--paper); }

  .section-title { font-family: "Montserrat", sans-serif; font-weight: 300; font-size: 27px; letter-spacing: 0.55em; color: var(--paper); }
  .chart-label { font-family: "Montserrat", sans-serif; font-weight: 300; font-size: 24px; letter-spacing: 0.5em; color: var(--paper); }

  .share { font-family: "Roboto", sans-serif; font-style: italic; font-weight: 900; font-size: 38px; color: var(--paper); }
  .share sup { font-size: 20px; font-weight: 700; vertical-align: 14px; }

  .stat-number { font-family: "Roboto", sans-serif; font-style: italic; font-weight: 300; font-size: 58px; color: var(--paper); }
  .stat-label { font-family: "Roboto", sans-serif; font-style: italic; font-weight: 700; font-size: 22px; color: var(--ink); }
  .sales-total { font-family: "Roboto", sans-serif; font-style: italic; font-weight: 900; font-size: 41px; color: var(--paper); letter-spacing: 0.5px; }

  .intro { position: absolute; left: 137px; top: 757px; width: 575px; font-family: "Source Sans 3", sans-serif; font-size: 13.2px; line-height: 16.1px; color: var(--paper); text-align: justify; text-align-last: center; }

  .col-head { font-family: "Montserrat", sans-serif; font-weight: 400; font-size: 8px; color: var(--paper); }
  .layer-name { font-family: "Roboto", sans-serif; font-style: italic; font-weight: 900; font-size: 15px; }
  .layer-note { font-family: "Montserrat", sans-serif; font-size: 7.5px; letter-spacing: 0.3px; }
  .on-dark { color: var(--paper); }
  .on-light { color: var(--ink); }
  .others-note { font-family: "Roboto", sans-serif; font-weight: 900; font-size: 9.5px; letter-spacing: 2.5px; color: var(--faint); line-height: 14px; }
  .only-us { font-family: "Roboto", sans-serif; font-style: italic; font-weight: 300; font-size: 40px; color: var(--ghost); line-height: 38px; }
  .benefit { font-family: "Roboto", sans-serif; font-style: italic; font-weight: 900; font-size: 15px; color: var(--ink); }
</style>
</head>
<body>
<div class="sheet">

  <svg class="shapes" width="849" height="1200" viewBox="0 0 849 1200" aria-hidden="true">
    <!-- header band with diagonal cut -->
    <polygon points="0,19 181,19 72,186 0,186" fill="var(--ink)"/>
    <polygon points="199,18 849,19 849,186 86,186" fill="var(--ink)"/>
    <!-- main body -->
    <rect x="0" y="197" width="849" height="984" fill="var(--ink)"/>

    <!-- data chart panel -->
    <g class="data-chart">
      <rect x="106" y="317" width="277" height="151" fill="var(--ink-soft)"/>
      <rect x="106" y="342" width="277" height="25" fill="var(--ink-band)"/>
      <rect x="106" y="393" width="277" height="25" fill="var(--ink-band)"/>
      <rect x="106" y="443" width="277" height="25" fill="var(--ink-band)"/>
      <polyline points="120,434 150,420 183,397 205,398 226,387 248,370 269,374 290,340 312,346 333,328 355,310" fill="none" stroke="#3e5a66" stroke-width="1"/>
      <polyline points="349,311 355,310 353,316" fill="none" stroke="#3e5a66" stroke-width="1"/>
      <rect x="120" y="449" width="12.5" height="19" fill="var(--paper)"/>
      <rect x="141" y="439" width="12.5" height="29" fill="var(--aqua)"/>
      <rect x="163" y="428" width="12.5" height="40" fill="var(--steel)"/>
      <rect x="184" y="412" width="12.5" height="56" fill="var(--paper)"/>
      <rect x="205" y="414" width="12.5" height="54" fill="var(--aqua)"/>
      <rect x="226" y="403" width="12.5" height="65" fill="var(--steel)"/>
      <rect x="248" y="375" width="12.5" height="93" fill="var(--paper)"/>
      <rect x="269" y="383" width="12.5" height="85" fill="var(--aqua)"/>
      <rect x="290" y="356" width="12.5" height="112" fill="var(--steel)"/>
      <rect x="312" y="366" width="12.5" height="102" fill="var(--paper)"/>
      <rect x="333" y="349" width="12.5" height="119" fill="var(--aqua)"/>
      <rect x="354" y="332" width="12.5" height="136" fill="var(--paper)"/>
    </g>

    <line x1="423" y1="328" x2="423" y2="459" stroke="var(--paper)" stroke-width="2"/>

    <!-- product type frames -->
    <g fill="none" stroke="var(--aqua)" stroke-width="1.6">
      <polygon points="477,406 564,406 545,459 450,459"/>
      <polygon points="582,406 679,406 660,459 565,459"/>
      <polygon points="697,406 794,406 775,459 680,459"/>
    </g>

    <!-- stat labels -->
    <g fill="var(--mist)">
      <polygon points="182,593 320,593 306,620 169,620"/>
      <polygon points="336,593 473,593 459,620 323,620"/>
      <polygon points="494,593 712,593 698,620 481,620"/>
    </g>

    <!-- sales frame -->
    <polygon points="168,629 696,629 665,712 137,712" fill="none" stroke="var(--paper)" stroke-width="1.5"/>

    <!-- competitors table -->
    <g class="lifecycle">
      <line x1="319" y1="936" x2="298" y2="978" stroke="var(--paper)" stroke-width="1"/>
      <polygon points="209,949 583,949 566,982 192,982" fill="none" stroke="var(--paper)" stroke-width="1.3"/>
      <line x1="317" y1="949" x2="298" y2="982" stroke="var(--paper)" stroke-width="1.3"/>
      <polygon points="588,949 658,949 640,982 571,982" fill="none" stroke="var(--paper)" stroke-width="1.3"/>
      <path d="M336 965 h10 M341 960 v10" stroke="var(--paper)" stroke-width="2.4"/>
      <line x1="355" y1="965" x2="538" y2="965" stroke="var(--paper)" stroke-width="1" stroke-dasharray="5 4"/>
      <path d="M543 960 l8 10 M551 960 l-8 10" stroke="var(--paper)" stroke-width="2.6"/>
      <path d="M609 965 h11 M614.5 959.5 v11" stroke="var(--paper)" stroke-width="2.4"/>

      <rect x="192" y="983" width="448" height="126" fill="var(--mist)"/>
      <line x1="192" y1="1028" x2="640" y2="1028" stroke="var(--ink)" stroke-width="0.8"/>
      <line x1="192" y1="1069" x2="640" y2="1069" stroke="var(--ink)" stroke-width="0.8"/>
      <g stroke="var(--ink)" stroke-width="1.2">
        <line x1="296" y1="990" x2="296" y2="1022"/>
        <line x1="296" y1="1033" x2="296" y2="1064"/>
        <line x1="296" y1="1073" x2="296" y2="1105"/>
      </g>
      <!-- row icons -->
      <g fill="none" stroke="var(--ink)" stroke-width="1.1">
        <circle cx="206" cy="1007" r="8"/>
        <ellipse cx="206" cy="1007" rx="3.5" ry="8"/>
        <line x1="198" y1="1007" x2="214" y2="1007"/>
        <line x1="199.5" y1="1003" x2="212.5" y2="1003"/>
        <line x1="199.5" y1="1011" x2="212.5" y2="1011"/>
        <path d="M198 1057 V1041 H217"/>
        <path d="M201 1045 h9 M201 1049 h9 M201 1053 h7 M205 1043 v14 M211 1045 h5 M213.5 1042.5 v5"/>
        <circle cx="207" cy="1087" r="3.2"/>
        <path d="M200.5 1097 a6.5 6 0 0 1 13 0"/>
      </g>
      <!-- benefit arrows -->
      <g fill="none" stroke="var(--ink)" stroke-width="1.1">
        <path d="M415 995 c0 12 8 16 28 16"/><path d="M438 1006 l5 5 l-5 5"/>
        <path d="M415 1035 c0 12 8 16 28 16"/><path d="M438 1046 l5 5 l-5 5"/>
        <path d="M415 1076 c0 12 8 16 28 16"/><path d="M438 1087 l5 5 l-5 5"/>
      </g>
    </g>
  </svg>

  <!-- header -->
  <div class="abs center brand" style="left:425px; top:64px;">ORVEN</div>

  <!-- market analysis -->
  <div class="abs center section-title" style="left:434px; top:257px;">MARKET ANALYSIS</div>
  <div class="abs chart-label" style="left:166px; top:346px;">DATA</div>
  <div class="abs chart-label" style="left:481px; top:346px;">PRODUCT TYPES</div>

  <div class="abs center share" style="left:508px; top:416px;">40<sup>%</sup></div>
  <div class="abs center share" style="left:623px; top:416px;">30<sup>%</sup></div>
  <div class="abs center share" style="left:742px; top:416px;">20<sup>%</sup></div>

  <div class="abs center stat-number" style="left:260px; top:533px;">20</div>
  <div class="abs center stat-number" style="left:403px; top:533px;">150</div>
  <div class="abs center stat-number" style="left:594px; top:533px;">350,000</div>

  <div class="abs center stat-label" style="left:242px; top:597px;">VENDORS</div>
  <div class="abs center stat-label" style="left:398px; top:597px;">PRODUCTS</div>
  <div class="abs center stat-label" style="left:596px; top:597px;">AVAILABLE ITEMS</div>

  <div class="abs center sales-total" style="left:419px; top:650px;">40 MILLION IN SALES</div>

  <p class="intro">Lorem ipsum dolor sit amet, consectetuer adipiscing elit, sed diam nonummy nibh euismod tincidunt ut laoreet dolore magna aliquam erat volutpat. Ut wisi enim ad minim veniam, quis nostrud exerci tation ullamcorper suscipit lobortis nisl ut aliquip ex ea commodo consequat. Duis autem vel eum iriure dolor in hendrerit in vulputate velit esse molestie consequat, vel illum</p>

  <!-- competitors -->
  <div class="abs center section-title" style="left:434px; top:881px;">COMPETITORS</div>

  <div class="abs center col-head" style="left:264px; top:935px;">PRODUCT LIFECYCLE</div>
  <div class="abs center col-head" style="left:345px; top:935px;">STEP 1</div>
  <div class="abs center col-head" style="left:417px; top:935px;">STEP 2</div>
  <div class="abs center col-head" style="left:488px; top:935px;">STEP 3</div>
  <div class="abs center col-head" style="left:560px; top:935px;">STEP 4</div>
  <div class="abs center col-head" style="left:615px; top:935px;">AGAIN</div>

  <div class="abs center layer-name on-dark" style="left:252px; top:955px;">LAYER 1</div>
  <div class="abs center layer-note on-dark" style="left:253px; top:970px;">Lorem Ipsum</div>
  <div class="abs center others-note" style="left:440px; top:952px;">THIS IS WHAT<br>OTHERS DO</div>

  <div class="abs center layer-name on-light" style="left:252px; top:996px;">LAYER 2</div>
  <div class="abs center layer-note on-light" style="left:252px; top:1012px;">Web Level</div>
  <div class="abs center layer-name on-light" style="left:252px; top:1035px;">LAYER 3</div>
  <div class="abs center layer-note on-light" style="left:252px; top:1051px;">Entity Level</div>
  <div class="abs center layer-name on-light" style="left:252px; top:1075px;">LAYER 4</div>
  <div class="abs center layer-note on-light" style="left:249px; top:1091px;">Personal Level</div>

  <div class="abs center only-us" style="left:355px; top:1008px;">ONLY<br>US</div>

  <div class="abs benefit" style="left:456px; top:1002px;">OUR BENEFIT</div>
  <div class="abs benefit" style="left:575px; top:1002px;">EFFECT</div>
  <div class="abs benefit" style="left:456px; top:1042px;">OUR BENEFIT</div>
  <div class="abs benefit" style="left:575px; top:1042px;">EFFECT</div>
  <div class="abs benefit" style="left:456px; top:1081px;">OUR BENEFIT</div>
  <div class="abs benefit" style="left:575px; top:1081px;">EFFECT</div>

</div>
</body>
</html>
```